64 on Birch Apartment Mailer to Competition

I need a postcard mailer designed that will be promoting a new apartment building in downtown Rochester NY. The postcards are being mailed to other apartment communities the we are in direct competition with. I have enclosed a bunch of info to guide you.

Target Market(s)

Other communities in the market

Industry/Entity Type

Property Management

Requirements
Must have
• Exterior rendering, features. Fit standard postcard, colors similar to enclosed, grey, white coral
Nice to have
• Interior Pictures

```html
<!DOCTYPE html>
<html lang="en">
<head>
<meta charset="utf-8">
<title>64 on Birch – Postcard Mailer</title>
<link rel="stylesheet" href="https://fonts.googleapis.com/css2?family=Questrial&family=Mulish:ital,wght@0,400;0,700;1,700&family=Oswald:wght@500&display=swap">
<style>
  :root {
    --ink: #24232b;
    --coral: #f9605c;
    --white: #ffffff;
    --text-soft: #ecebef;
    --sheet-grey: #e4e4e4;
    --page: #ffffff;
  }
  * { margin: 0; padding: 0; box-sizing: border-box; }
  html, body { width: 862px; height: 1200px; overflow: hidden; background: var(--page); }
  .canvas { position: relative; width: 862px; height: 1200px; }

  /* ---------- Front ---------- */
  .front {
    position: absolute; left: 0; top: 0; width: 862px; height: 616px;
    background: var(--ink); overflow: hidden;
    font-family: "Questrial", "Century Gothic", sans-serif; color: var(--text-soft);
  }
  .front-art { position: absolute; left: 0; top: 0; }
  .leasing-ribbon {
    position: absolute; left: 262px; top: 64px; width: 190px;
    transform: rotate(38deg); transform-origin: center;
    color: var(--white); font-family: "Questrial", sans-serif;
    font-size: 14px; letter-spacing: 1.5px; line-height: 18px; text-align: center;
  }
  .brand {
    position: absolute; left: 39px; top: 196px;
    display: flex; align-items: center; gap: 14px;
  }
  .brand-mark { width: 34px; height: 34px; background: var(--white); }
  .brand-name { font-size: 30px; color: var(--white); letter-spacing: 0.5px; }
  .tagline {
    position: absolute; left: 30px; top: 250px;
    color: var(--coral); font-size: 16.5px;
  }
  .intro {
    position: absolute; left: 30px; top: 285px; width: 385px;
    font-size: 14.6px; line-height: 21px; color: var(--text-soft);
  }
  .leasing-title {
    position: absolute; left: 30px; top: 398px;
    color: var(--coral); font-size: 16.5px;
  }
  .leasing-units { position: absolute; left: 30px; top: 422px; font-size: 14.6px; }
  .tour-call {
    position: absolute; left: 62px; top: 478px; width: 110px;
    font-family: "Oswald", sans-serif; text-align: center;
    font-size: 15px; letter-spacing: 1.6px; line-height: 24px; color: var(--white);
  }
  .tour-call .accent { display: block; color: var(--coral); font-size: 19px; margin-top: 4px; }
  .contact-list { position: absolute; left: 216px; top: 468px; list-style: none; }
  .contact-list li { display: flex; align-items: flex-start; gap: 10px; color: var(--text-soft); }
  .contact-list .big { font-size: 18.5px; height: 28px; line-height: 24px; }
  .contact-list .small { font-size: 14.6px; line-height: 19px; margin-top: 4px; }
  .contact-list svg { flex: none; margin-top: 4px; }

  /* ---------- Back ---------- */
  .back {
    position: absolute; left: 0; top: 626px; width: 420px; height: 574px;
    background: var(--ink); overflow: hidden;
    font-family: "Mulish", "Century Gothic", sans-serif; color: var(--text-soft);
  }
  .back-sheet {
    position: absolute; left: 420px; top: 626px; width: 442px; height: 574px;
    background: var(--sheet-grey);
  }
  .contact-band {
    position: absolute; left: 0; top: 41px; width: 420px; height: 68px;
    background: var(--coral); color: var(--white);
    padding: 7px 0 0 155px; font-size: 13.5px; line-height: 18px;
  }
  .contact-band .band-title { font-weight: 700; font-style: italic; font-size: 14px; }
  .brand-tile {
    position: absolute; left: 20px; top: 24px; width: 124px; height: 108px;
    background: var(--coral); border: 1.5px solid var(--white);
    display: flex; align-items: flex-end; justify-content: center; padding-bottom: 8px;
  }
  .brand-tile .brand-name { font-family: "Questrial", sans-serif; font-size: 17px; }
  .section-title {
    position: absolute; left: 0; width: 398px; text-align: center;
    color: var(--coral); font-weight: 700; font-size: 12px;
  }
  .spec-list { position: absolute; left: 35px; width: 370px; list-style: none; font-size: 12.5px; line-height: 17px; }
  .spec-list li { position: relative; padding-left: 28px; margin-bottom: 0.5px; }
  .spec-list li::before { content: "★"; position: absolute; left: 0; top: 0; font-size: 11px; color: var(--white); }
  .more-note {
    position: absolute; left: 0; top: 417px; width: 398px; text-align: center;
    color: var(--coral); font-weight: 700; font-style: italic; font-size: 13px;
  }
  .interior-photo { position: absolute; top: 438px; height: 117px; border: 1px solid var(--white); }
  .interior-living { left: 20px; width: 210px; background: linear-gradient(160deg, #e9e7e3 0%, #c9c3bb 55%, #5b4a3c 100%); }
  .interior-kitchen { left: 237px; width: 176px; background: linear-gradient(170deg, #d6d4d0 0%, #8d8780 45%, #3a3431 100%); }
</style>
</head>
<body>
<main class="canvas">

  <section class="front">
    <svg class="front-art" width="862" height="616" viewBox="0 0 862 616" role="img" aria-label="Exterior rendering of the glass apartment tower at dusk with lit units and street trees">
      <defs>
        <linearGradient id="tower-render" x1="0" y1="0" x2="0" y2="1">
          <stop offset="0" stop-color="#8aa3bd"/>
          <stop offset="0.35" stop-color="#b9c7d4"/>
          <stop offset="0.7" stop-color="#94a8b8"/>
          <stop offset="1" stop-color="#4d5a5c"/>
        </linearGradient>
      </defs>
      <polygon points="413,0 862,0 862,616 512,616" fill="url(#tower-render)"/>
    </svg>
    <svg class="front-art" width="862" height="616" viewBox="0 0 862 616" aria-hidden="true">
      <polygon points="180,0 413,0 447,209" fill="var(--coral)"/>
    </svg>
    <div class="leasing-ribbon">NOW LEASING<br>BRAND NEW APARTMENTS</div>

    <div class="brand">
      <span class="brand-mark"></span>
      <span class="brand-name">64 ON BIRCH</span>
    </div>

    <p class="tagline">Luxury, Location and Convenience.</p>
    <p class="intro">The newest addition to Rochester. Enjoy all that modern living has to offer. Whether it's enjoying a warm summer evening on the rooftop patio or exploring what Downtown Rochester has to offer, 64 on Birch is truly the ideal location.</p>
    <p class="leasing-title">NOW LEASING</p>
    <p class="leasing-units">1 and 2 bedroom units, from $1,400.</p>

    <p class="tour-call">CONTACT US<br>TO SCHEDULE<span class="accent">A TOUR</span></p>

    <ul class="contact-list">
      <li class="big">
        <svg width="17" height="17" viewBox="0 0 20 20" fill="none" stroke="var(--coral)" stroke-width="1.8"><circle cx="10" cy="10" r="8.5"/><ellipse cx="10" cy="10" rx="3.8" ry="8.5"/><line x1="1.5" y1="10" x2="18.5" y2="10"/><line x1="3" y1="5.5" x2="17" y2="5.5"/><line x1="3" y1="14.5" x2="17" y2="14.5"/></svg>
        <span>www.64onbirch.com</span>
      </li>
      <li class="big">
        <svg width="17" height="17" viewBox="0 0 20 20" fill="none" stroke="var(--coral)" stroke-width="1.8" stroke-linejoin="round"><path d="M4 2 L7.5 2 L9 6.5 L6.8 8 C8 10.8 9.6 12.5 12 13.4 L13.5 11.2 L18 12.7 L18 16 C18 17.2 17 18 15.8 18 C8.5 17.5 2.5 11.5 2 4.2 C2 3 2.8 2 4 2 Z"/></svg>
        <span>(585) 555-0164</span>
      </li>
      <li class="small">
        <svg width="14" height="18" viewBox="0 0 14 18"><path d="M7 0 C3.1 0 0 3 0 6.8 C0 11.5 7 18 7 18 C7 18 14 11.5 14 6.8 C14 3 10.9 0 7 0 Z" fill="var(--coral)"/><circle cx="7" cy="6.8" r="2.6" fill="var(--ink)"/></svg>
        <span>64 Birch Street<br>Rochester, NY 14604</span>
      </li>
    </ul>
  </section>

  <section class="back">
    <div class="contact-band">
      <p class="band-title">CONTACT US TO SCHEDULE A TOUR</p>
      <p>64 Birch Street. Rochester, NY 14604</p>
      <p>585.555.0164 | www.64onbirch.com</p>
    </div>
    <div class="brand-tile"><span class="brand-name">64 ON BIRCH</span></div>

    <h2 class="section-title" style="top:141px">FLOORPLANS</h2>
    <ul class="spec-list" style="top:157px">
      <li>1 Bedroom, 1 Bedroom with Den, and 2<br>Bedroom 2 Bath Available</li>
      <li>$1400 to $3300</li>
      <li>&nbsp;775 to 1677 sq. ft.</li>
      <li>Open Floor Plans with Contemporary Features</li>
      <li>Hardwood Flooring, W/D In Unit, LED Lighting</li>
      <li>Granite Countertops, Undermount Sinks, Tile<br>backsplash, Walk-In Closets Available</li>
    </ul>

    <h2 class="section-title" style="top:300px">FEATURES</h2>
    <ul class="spec-list" style="top:316px">
      <li>Amazing Views with a Rooftop Patio</li>
      <li>24 Hour Fitness</li>
      <li>High Speed Internet, Cable, Heat, and A/C included.<br>Parking Available, One Spot Included</li>
      <li>Modern Controlled Access</li>
    </ul>

    <p class="more-note">And much more!</p>

    <div class="interior-photo interior-living" role="img" aria-label="Interior photo of a bright open living room with white sofa and wood floors"></div>
    <div class="interior-photo interior-kitchen" role="img" aria-label="Interior photo of a modern kitchen with granite island and bar stools"></div>
  </section>

  <div class="back-sheet" aria-hidden="true"></div>

</main>
</body>
</html>
```